New Business Cards for Torvin Group

We need a new Business Card to compliment our new logo. We are a vibrant design, manufacture and install business providing recreation areas, public parks and Municipal spaces. We want business cards that are classy, modern and clean.

We have recently changed our logo, and are celebrating our 40th anniversary. We want business cards with a new modern design to reflect our status.

Target Market(s)

Customers

Contact Information for Business Card

We need all the details of our 3 offices as per the business card attached. Please disregard the old logo on the business card, the other three files show our new logo.

Requirements
Must have
• All info as per attached business card but with new logo.
Nice to have

```html
<!DOCTYPE html>
<html lang="en">
<head>
<meta charset="utf-8">
<title>Torvin Group – Business Cards</title>
<link href="https://fonts.googleapis.com/css2?family=Roboto:wght@400;500;700&display=swap" rel="stylesheet">
<style>
  :root {
    --backdrop: #3a3533;
    --card-white: #f4f4f4;
    --brand-red: #ec3038;
    --ink-dark: #4a4a4a;
    --ink-mid: #555555;
    --rule-grey: #9a9a9a;
    --text-on-red: #ffffff;
    --faint-on-red: rgba(160, 20, 28, 0.28);
  }
  * { margin: 0; padding: 0; box-sizing: border-box; }
  html, body {
    width: 1200px; height: 844px; overflow: hidden;
    background: var(--backdrop);
    font-family: "Roboto", Arial, sans-serif;
  }
  .canvas { position: relative; width: 1200px; height: 844px; }

  .card {
    position: absolute;
    width: 540px; height: 310px;
    box-shadow: 0 12px 30px rgba(0,0,0,0.45);
  }

  /* Front */
  .card-front { left: 60px; top: 430px; background: var(--card-white); }
  .brand {
    position: absolute; left: 40px; top: 134px;
    width: 236px;
    display: flex; align-items: center; gap: 10px;
    white-space: nowrap;
  }
  .brand-dot {
    width: 36px; height: 36px; border-radius: 50%;
    background: var(--brand-red); flex: none;
  }
  .brand-name {
    font-weight: 700; font-size: 22px; color: var(--brand-red);
    letter-spacing: 0.3px; text-transform: uppercase;
  }
  .divider {
    position: absolute; left: 296px; top: 92px;
    width: 1px; height: 120px; background: var(--rule-grey);
  }
  .contact { position: absolute; left: 320px; top: 94px; }
  .contact-name {
    font-weight: 500; font-size: 20px; color: var(--brand-red);
    text-transform: uppercase; letter-spacing: 0.3px;
  }
  .contact-role { font-size: 14px; color: var(--ink-mid); margin-bottom: 18px; }
  .contact-line {
    display: flex; align-items: center; gap: 8px;
    font-size: 14px; color: var(--ink-dark); line-height: 20px;
  }
  .contact-line svg { width: 12px; height: 12px; fill: var(--brand-red); flex: none; }

  /* Back */
  .card-back {
    left: 620px; top: 110px; background: var(--brand-red);
    overflow: hidden; color: var(--text-on-red);
  }
  .back-mark {
    position: absolute; left: 60px; top: 30px;
    width: 250px; height: 250px; border-radius: 50%;
    background: var(--faint-on-red);
  }
  .office { position: absolute; font-size: 11.5px; line-height: 15px; }
  .office-title { font-weight: 700; font-size: 14px; margin-bottom: 2px; }
  .office-head { left: 200px; top: 28px; text-align: right; }
  .office-qatar { left: 370px; top: 140px; }
  .office-dubai { left: 40px; top: 200px; }
</style>
</head>
<body>
<main class="canvas">
  <section class="card card-front">
    <div class="brand">
      <span class="brand-dot"></span>
      <span class="brand-name">Torvin Group</span>
    </div>
    <div class="divider"></div>
    <div class="contact">
      <p class="contact-name">Rami Haddane</p>
      <p class="contact-role">Managing Partner</p>
      <p class="contact-line">
        <svg viewBox="0 0 24 24" aria-hidden="true"><path d="M6.6 10.8a15.1 15.1 0 0 0 6.6 6.6l2.2-2.2c.3-.3.7-.4 1-.2 1.1.4 2.3.6 3.6.6.6 0 1 .4 1 1V20c0 .6-.4 1-1 1A17 17 0 0 1 3 4c0-.6.4-1 1-1h3.5c.6 0 1 .4 1 1 0 1.3.2 2.5.6 3.6.1.3 0 .7-.2 1z"/></svg>
        +971 (0)50 555 0148
      </p>
      <p class="contact-line">
        <svg viewBox="0 0 24 24" aria-hidden="true"><path d="M2 5h20v2l-10 7L2 7z M2 9.5l10 7 10-7V19H2z"/></svg>
        rami@torvingroup.com
      </p>
      <p class="contact-line">
        <svg viewBox="0 0 24 24" aria-hidden="true"><circle cx="12" cy="12" r="10"/></svg>
        www.torvingroup.com
      </p>
    </div>
  </section>

  <section class="card card-back">
    <div class="back-mark" aria-hidden="true"></div>
    <div class="office office-head">
      <p class="office-title">Head Office</p>
      <p>P.O.Box:10482 Abu Dhabi U.A.E.</p>
      <p>P : +971 (0)2 555 0161</p>
      <p>F : +971 (0)2 555 0162</p>
      <p>E : sales@torvingroup.com</p>
    </div>
    <div class="office office-qatar">
      <p class="office-title">Qatar Office</p>
      <p>P.O.Box:30591 Doha, Qatar</p>
      <p>P : +974 4455 0185</p>
      <p>F : +974 4455 0186</p>
      <p>E : sales@torvingroup.com</p>
    </div>
    <div class="office office-dubai">
      <p class="office-title">Dubai Office</p>
      <p>P.O.Box:204417 Dubai U.A.E.</p>
      <p>P : +971 (0)4 555 0173</p>
      <p>F : +971 (0)4 555 0174</p>
      <p>E : sales@torvingroup.com</p>
    </div>
  </section>
</main>
</body>
</html>
```